Design for an iOS and Android app managing shopping list

The app allows you to keep manage shopping lists, each shopping list being made of items to buy...
We need a design for the 3 screens of the app:
a) global view showing list of (shopping) list
b) form enabling to edit the name of a (shopping) list
c) detailed view listing the contents/items of a (shopping) list
d) 1 text page [not illustrated]
2 "alerts" items are also to be designed: confirm and error pop ups.
No specific guidelines, nor logo or whatever.
It will be a free app distributed on iOS and Androïd.
We just want to make it looking nice & very usable for end users.

```html
<!DOCTYPE html>
<html lang="en">
<head>
<meta charset="utf-8">
<title>Shopping Lists – App Screens</title>
<link href="https://fonts.googleapis.com/css2?family=Roboto:wght@300;400;500&display=swap" rel="stylesheet">
<style>
  :root {
    --backdrop: #2dd6d6;
    --bar-black: #000;
    --appbar-top: #2c3135;
    --appbar-bottom: #0d0f11;
    --screen-bg: #f8f8f8;
    --field-bg: #cfd8dd;
    --slate: #37474f;
    --blue-grey: #607d8b;
    --ink: #2f3437;
    --muted: #8e9aa1;
    --divider: #e2e5e7;
    --keyboard-bg: #ececec;
    --key-ink: #737373;
    --action-blue: #2196f3;
    --approved: #6cc04a;
    --pending: #f5c518;
    --white: #fff;
  }
  * { box-sizing: border-box; margin: 0; padding: 0; }
  html, body { width: 1082px; height: 1200px; overflow: hidden; }
  body { background: var(--backdrop); font-family: 'Roboto', sans-serif; }
  .stage { position: relative; width: 1352px; height: 1500px; transform: scale(.8); transform-origin: 0 0; }

  .screen { position: absolute; width: 400px; height: 709px; background: var(--screen-bg); overflow: hidden; }
  .screen.s1 { left: 62px; top: 37px; }
  .screen.s2 { left: 476px; top: 37px; }
  .screen.s3 { left: 890px; top: 37px; }
  .screen.s4 { left: 270px; top: 755px; }
  .screen.s5 { left: 684px; top: 755px; }

  .status-bar { position: absolute; top: 0; left: 0; right: 0; height: 26px; background: var(--bar-black); color: var(--white);
    display: flex; justify-content: flex-end; align-items: center; gap: 8px; padding-right: 8px; font-size: 13px; }
  .status-bar svg { width: 12px; height: 12px; fill: var(--white); }
  .app-bar { position: absolute; top: 26px; left: 0; right: 0; height: 62px; background: linear-gradient(var(--appbar-top), var(--appbar-bottom));
    color: var(--white); display: flex; align-items: center; padding-left: 18px; font-size: 18px; }
  .app-bar svg { width: 12px; height: 14px; margin-right: 12px; stroke: var(--white); fill: none; stroke-width: 2; }
  .nav-bar { position: absolute; bottom: 0; left: 0; right: 0; height: 53px; background: var(--bar-black); }
  .nav-bar svg { position: absolute; top: 14px; width: 26px; height: 26px; fill: none; stroke: var(--white); stroke-width: 2; }
  .nav-bar .back { left: 76px; } .nav-bar .home { left: 187px; } .nav-bar .recent { left: 299px; }

  .name-field { position: absolute; left: 19px; top: 126px; width: 362px; height: 59px; background: var(--field-bg);
    padding-left: 14px; display: flex; align-items: center; font-size: 17px; font-weight: 500; color: #4e5b62; }
  .save-button { position: absolute; left: 19px; top: 203px; width: 362px; height: 40px; background: var(--slate);
    color: var(--white); font-size: 17px; font-weight: 500; display: flex; align-items: center; justify-content: center; box-shadow: 0 2px 3px rgba(0,0,0,.25); }

  .keyboard { position: absolute; left: 0; right: 0; top: 405px; height: 251px; background: var(--keyboard-bg); color: var(--key-ink); font-weight: 300; }
  .key-row { position: absolute; left: 0; right: 0; height: 40px; display: flex; align-items: center; font-size: 24px; }
  .key-row span { position: relative; text-align: center; flex: 0 0 38.9px; }
  .key-row sup { position: absolute; top: -14px; right: 8px; font-size: 10px; }
  .row-1 { top: 25px; padding-left: 6px; }
  .row-2 { top: 82px; padding-left: 25px; }
  .row-3 { top: 140px; padding-left: 14px; }
  .row-3 .wide { flex-basis: 49px; }
  .row-3 svg { width: 22px; height: 20px; fill: #bdbdbd; }
  .row-4 { top: 196px; }
  .row-4 > * { position: absolute; }
  .row-4 .symbols { left: 17px; font-size: 13px; }
  .row-4 .mic { left: 76px; width: 14px; height: 22px; fill: var(--key-ink); }
  .row-4 .space { left: 117px; width: 166px; height: 24px; background: #d6d6d6; }
  .row-4 .slash { left: 310px; }
  .row-4 .kb { left: 354px; width: 22px; height: 20px; fill: var(--key-ink); }

  .dialog { position: absolute; background: var(--white); box-shadow: 0 6px 18px rgba(0,0,0,.3); border-radius: 2px; }
  .dialog h2 { font-size: 21px; font-weight: 400; color: var(--ink); }
  .dialog p { font-size: 17px; line-height: 27px; color: var(--ink); margin-top: 14px; }
  .dialog .actions { display: flex; justify-content: space-between; margin-top: 14px; color: var(--action-blue); font-size: 17px; font-weight: 500; }
  .warning { left: 48px; top: 221px; width: 310px; height: 170px; padding: 26px 22px 0 22px; }
  .warning p { margin-top: 10px; padding-left: 6px; }
  .warning .actions { justify-content: flex-end; margin-top: 4px; padding-right: 0; }
  .confirm { left: 17px; top: 183px; width: 363px; height: 188px; padding: 26px 21px 0 21px; z-index: 2; }
  .confirm p { margin-top: 12px; }
  .confirm .actions { margin-top: 16px; }

  .new-list { position: absolute; left: 19px; top: 125px; width: 362px; height: 44px; background: var(--field-bg); border-radius: 22px;
    display: flex; align-items: center; overflow: hidden; font-size: 17px; font-weight: 300; color: var(--muted); }
  .new-list .edit { width: 46px; height: 44px; background: var(--slate); display: flex; align-items: center; justify-content: center; margin-right: 2px; border-radius: 22px 0 0 22px; }
  .new-list .edit svg { width: 24px; height: 24px; fill: none; stroke: var(--white); stroke-width: 1.8; }

  .lists { position: absolute; left: 0; right: 0; top: 196px; list-style: none; }
  .lists li { position: relative; height: 66.6px; border-top: 1px solid var(--divider); display: flex; align-items: center; padding-left: 33px;
    font-size: 17px; font-weight: 500; color: var(--ink); }
  .lists li:last-child { border-bottom: 1px solid var(--divider); }
  .lists .trash { position: absolute; right: 30px; width: 20px; height: 22px; fill: none; stroke: var(--slate); stroke-width: 1.6; }
  .lists .state { position: absolute; left: 170px; font-size: 13px; font-weight: 400; display: flex; align-items: center; gap: 3px; }
  .lists .state svg { width: 12px; height: 12px; fill: currentColor; }
  .state.approved { color: var(--approved); }
  .state.pending { color: var(--pending); }

  .about-button { position: absolute; left: 138px; top: 605px; width: 124px; height: 40px; background: var(--blue-grey);
    color: var(--white); font-size: 15px; font-weight: 500; display: flex; align-items: center; justify-content: center; box-shadow: 0 2px 4px rgba(0,0,0,.3); }
</style>
</head>
<body>
<svg width="0" height="0" style="position:absolute">
  <defs>
    <symbol id="i-wifi" viewBox="0 0 12 12"><path d="M0 2 Q6 -1 12 2 L6 11 Z"/></symbol>
    <symbol id="i-signal" viewBox="0 0 12 12"><path d="M12 0 V12 H0 Z"/></symbol>
    <symbol id="i-battery" viewBox="0 0 12 12"><rect x="3" y="1" width="6" height="11"/><rect x="4.5" y="0" width="3" height="1"/></symbol>
    <symbol id="i-chevron" viewBox="0 0 12 14"><path d="M8 1 L2 7 L8 13"/></symbol>
    <symbol id="i-trash" viewBox="0 0 20 22"><path d="M1 4 H19 M7 4 V1.5 H13 V4 M3 4 L4 21 H16 L17 4 M8 8 V18 M12 8 V18"/></symbol>
    <symbol id="i-edit" viewBox="0 0 24 24"><path d="M17 13 V20 H4 V7 H11 M10 15 L11 11 L19 3 L22 6 L14 14 Z"/></symbol>
    <symbol id="i-tick" viewBox="0 0 12 12"><path d="M0 6.5 L2 4.5 L4.5 7 L10 1.5 L12 3.5 L4.5 11 Z"/></symbol>
    <symbol id="i-shift" viewBox="0 0 22 20"><path d="M11 1 L21 11 H15 V19 H7 V11 H1 Z"/></symbol>
    <symbol id="i-backspace" viewBox="0 0 22 20"><path d="M7 3 H21 V17 H7 L1 10 Z M10 6 L16 14 M16 6 L10 14" stroke="#ececec" stroke-width="2"/></symbol>
    <symbol id="i-mic" viewBox="0 0 14 22"><rect x="4" y="0" width="6" height="13" rx="3"/><path d="M1 10 Q1 17 7 17 Q13 17 13 10 H12 Q12 16 7 16 Q2 16 2 10 Z M6 17 H8 V22 H6 Z"/></symbol>
    <symbol id="i-keyboard" viewBox="0 0 22 20"><path d="M1 1 H21 V13 H1 Z M3 3 V5 H5 V3 Z M7 3 V5 H9 V3 Z M11 3 V5 H13 V3 Z M15 3 V5 H17 V3 Z M3 7 V9 H5 V7 Z M17 7 V9 H19 V7 Z M6 10 V11 H16 V10 Z M8 15 H14 L11 19 Z" fill-rule="evenodd"/></symbol>
    <symbol id="i-back" viewBox="0 0 26 26"><path d="M22 2 L3 13 L22 24 Z"/></symbol>
    <symbol id="i-home" viewBox="0 0 26 26"><circle cx="13" cy="13" r="11.5"/></symbol>
    <symbol id="i-recent" viewBox="0 0 26 26"><rect x="2" y="2" width="22" height="22"/></symbol>
  </defs>
</svg>

<main class="stage">

  <!-- Edit list name: validation error -->
  <section class="screen s1">
    <div class="status-bar"><svg><use href="#i-wifi"/></svg><svg><use href="#i-signal"/></svg><svg><use href="#i-battery"/></svg><span>15:45</span></div>
    <header class="app-bar"><svg><use href="#i-chevron"/></svg>Update list name</header>
    <div class="name-field"></div>
    <div class="save-button">SAVE</div>
    <div class="keyboard">
      <div class="key-row row-1"><span>q<sup>2</sup></span><span>w<sup>3</sup></span><span>e<sup>4</sup></span><span>r<sup>5</sup></span><span>t<sup>6</sup></span><span>y<sup>7</sup></span><span>u<sup>8</sup></span><span>i<sup>9</sup></span><span>o<sup>:</sup></span><span>p<sup>1</sup></span></div>
      <div class="key-row row-2"><span>a</span><span>s</span><span>d</span><span>f</span><span>g</span><span>h</span><span>j</span><span>k</span><span>l</span></div>
      <div class="key-row row-3"><span class="wide"><svg><use href="#i-shift"/></svg></span><span>z</span><span>x</span><span>c</span><span>v</span><span>b</span><span>n</span><span>m</span><span class="wide"><svg><use href="#i-backspace"/></svg></span></div>
      <div class="key-row row-4"><span class="symbols">@234</span><svg class="mic"><use href="#i-mic"/></svg><span class="space"></span><span class="slash">/</span><svg class="kb"><use href="#i-keyboard"/></svg></div>
    </div>
    <div class="dialog warning">
      <h2>Warning</h2>
      <p>List name should have at least 1 charcter to be valid!</p>
      <div class="actions"><span>ok</span></div>
    </div>
    <nav class="nav-bar"><svg class="back"><use href="#i-back"/></svg><svg class="home"><use href="#i-home"/></svg><svg class="recent"><use href="#i-recent"/></svg></nav>
  </section>

  <!-- Edit list name -->
  <section class="screen s2">
    <div class="status-bar"><svg><use href="#i-wifi"/></svg><svg><use href="#i-signal"/></svg><svg><use href="#i-battery"/></svg><span>15:45</span></div>
    <header class="app-bar"><svg><use href="#i-chevron"/></svg>Update list name</header>
    <div class="name-field">Diner de ce soir</div>
    <div class="save-button">SAVE</div>
    <div class="keyboard">
      <div class="key-row row-1"><span>q<sup>2</sup></span><span>w<sup>3</sup></span><span>e<sup>4</sup></span><span>r<sup>5</sup></span><span>t<sup>6</sup></span><span>y<sup>7</sup></span><span>u<sup>8</sup></span><span>i<sup>9</sup></span><span>o<sup>:</sup></span><span>p<sup>1</sup></span></div>
      <div class="key-row row-2"><span>a</span><span>s</span><span>d</span><span>f</span><span>g</span><span>h</span><span>j</span><span>k</span><span>l</span></div>
      <div class="key-row row-3"><span class="wide"><svg><use href="#i-shift"/></svg></span><span>z</span><span>x</span><span>c</span><span>v</span><span>b</span><span>n</span><span>m</span><span class="wide"><svg><use href="#i-backspace"/></svg></span></div>
      <div class="key-row row-4"><span class="symbols">@234</span><svg class="mic"><use href="#i-mic"/></svg><span class="space"></span><span class="slash">/</span><svg class="kb"><use href="#i-keyboard"/></svg></div>
    </div>
    <nav class="nav-bar"><svg class="back"><use href="#i-back"/></svg><svg class="home"><use href="#i-home"/></svg><svg class="recent"><use href="#i-recent"/></svg></nav>
  </section>

  <!-- Lists overview -->
  <section class="screen s3">
    <div class="status-bar"><svg><use href="#i-wifi"/></svg><svg><use href="#i-signal"/></svg><svg><use href="#i-battery"/></svg><span>15:45</span></div>
    <header class="app-bar"><svg><use href="#i-chevron"/></svg>Lists</header>
    <div class="new-list"><span class="edit"><svg><use href="#i-edit"/></svg></span>Add a new shopping list</div>
    <ul class="lists">
      <li>Diner de ce soir<svg class="trash"><use href="#i-trash"/></svg></li>
      <li>Course Noel<svg class="trash"><use href="#i-trash"/></svg></li>
      <li>Courses Maisonnet<svg class="trash"><use href="#i-trash"/></svg></li>
      <li>Marchemont<svg class="trash"><use href="#i-trash"/></svg></li>
      <li>Menage<svg class="trash"><use href="#i-trash"/></svg></li>
      <li>Cadeaux de noel<svg class="trash"><use href="#i-trash"/></svg></li>
    </ul>
    <div class="about-button">About Us</div>
    <nav class="nav-bar"><svg class="back"><use href="#i-back"/></svg><svg class="home"><use href="#i-home"/></svg><svg class="recent"><use href="#i-recent"/></svg></nav>
  </section>

  <!-- Lists overview: delete confirmation -->
  <section class="screen s4">
    <div class="status-bar"><svg><use href="#i-wifi"/></svg><svg><use href="#i-signal"/></svg><svg><use href="#i-battery"/></svg><span>15:45</span></div>
    <header class="app-bar"><svg><use href="#i-chevron"/></svg>Lists</header>
    <div class="new-list"><span class="edit"><svg><use href="#i-edit"/></svg></span>Add a new shopping list</div>
    <ul class="lists">
      <li>Diner de ce soir<svg class="trash"><use href="#i-trash"/></svg></li>
      <li>Course Noel<svg class="trash"><use href="#i-trash"/></svg></li>
      <li>Courses Maisonnet<svg class="trash"><use href="#i-trash"/></svg></li>
      <li>Marchemont<svg class="trash"><use href="#i-trash"/></svg></li>
      <li>Menage<svg class="trash"><use href="#i-trash"/></svg></li>
      <li>Cadeaux de noel<svg class="trash"><use href="#i-trash"/></svg></li>
    </ul>
    <div class="dialog confirm">
      <h2>Remove the shopping list</h2>
      <p>Would you like to delete the shopping list?</p>
      <div class="actions"><span>Cancel</span><span>Delete</span></div>
    </div>
    <div class="about-button">About Us</div>
    <nav class="nav-bar"><svg class="back"><use href="#i-back"/></svg><svg class="home"><use href="#i-home"/></svg><svg class="recent"><use href="#i-recent"/></svg></nav>
  </section>

  <!-- Lists overview with status -->
  <section class="screen s5">
    <div class="status-bar"><svg><use href="#i-wifi"/></svg><svg><use href="#i-signal"/></svg><svg><use href="#i-battery"/></svg><span>15:45</span></div>
    <header class="app-bar"><svg><use href="#i-chevron"/></svg>Lists</header>
    <div class="new-list"><span class="edit"><svg><use href="#i-edit"/></svg></span>Add a new shopping list</div>
    <ul class="lists">
      <li>Diner de ce soir<span class="state approved"><svg><use href="#i-tick"/></svg>Approved</span><svg class="trash"><use href="#i-trash"/></svg></li>
      <li>Course Noel<span class="state approved"><svg><use href="#i-tick"/></svg>Approved</span><svg class="trash"><use href="#i-trash"/></svg></li>
      <li>Courses Maisonnet<span class="state approved" style="left:184px"><svg><use href="#i-tick"/></svg>Approved</span><svg class="trash"><use href="#i-trash"/></svg></li>
      <li>Marchemont<span class="state approved"><svg><use href="#i-tick"/></svg>Approved</span><svg class="trash"><use href="#i-trash"/></svg></li>
      <li>Menage<span class="state pending"><svg><use href="#i-tick"/></svg>Pending</span><svg class="trash"><use href="#i-trash"/></svg></li>
      <li>Cadeaux de noel<span class="state pending"><svg><use href="#i-tick"/></svg>Pending</span><svg class="trash"><use href="#i-trash"/></svg></li>
    </ul>
    <nav class="nav-bar"><svg class="back"><use href="#i-back"/></svg><svg class="home"><use href="#i-home"/></svg><svg class="recent"><use href="#i-recent"/></svg></nav>
  </section>

</main>
</body>
</html>
```